6 - 8 'Holistic' Instagram Graphics

Hi there!
We are looking to build up a library of Graphic Templates to use as Instagram & Facebook posts for our Holistic Medi Spa (& 3 other companies eventually)
This competition is for a sample of 6 - 8 designs. For the winner(s), we will make an agreement for a batch order (Looking for 200+ designs in total), and will be looking to make a long term arrangement.
Please find a full job description in the attached Word Document.
Any questions, don't hesitate to ask.
Thanks!
Medical Spa

```html
<!DOCTYPE html>
<html lang="en">
<head>
<meta charset="utf-8">
<title>Willowmere – Holistic Post Templates</title>
<link rel="stylesheet" href="https://fonts.googleapis.com/css2?family=Quicksand:wght@500;600;700&family=Roboto:wght@500;700&family=Yellowtail&display=swap">
<style>
  :root {
    --board: #cccccc;
    --mint: #e1f3ef;
    --mint-deep: #7ccbbf;
    --sand: #f6eadf;
    --sand-texture: #e6d9c8;
    --ink: #141414;
    --muted: #7d7b72;
    --sage: #8eae97;
    --leaf: #3f8f3c;
    --leaf-dark: #2f7a35;
    --coral: #e2a190;
    --white: #ffffff;
  }
  * { margin: 0; padding: 0; box-sizing: border-box; }
  html, body { width: 1065px; height: 1200px; overflow: hidden; }
  body { background: var(--board); position: relative; font-family: "Quicksand", sans-serif; color: var(--ink); }

  .post { position: absolute; width: 460px; height: 460px; overflow: hidden; }
  .post--yoga { left: 56px; top: 114px; background: var(--mint); }
  .post--stones { left: 549px; top: 114px; background: var(--sand); }
  .post--massage { left: 56px; top: 625px; background: var(--sand); }
  .post--beach { left: 549px; top: 625px; background: var(--white); }

  .abs { position: absolute; }
  .photo { position: absolute; }

  .brand { position: absolute; display: flex; align-items: center; gap: 7px;
           font-family: "Quicksand", sans-serif; font-weight: 600; font-size: 20px; color: var(--muted); }
  .brand__dot { width: 18px; height: 18px; border-radius: 50%; background: var(--mint-deep); }

  .offer { font-family: "Roboto", sans-serif; font-weight: 500; color: var(--muted); }

  /* Post 1 */
  .leaf { position: absolute; background: var(--leaf); opacity: .85; }
  .leaf--palm-tl { left: -10px; top: -10px; width: 130px; height: 90px; border-radius: 0 0 90px 0; }
  .leaf--monstera-tr { left: 385px; top: -6px; width: 82px; height: 70px; border-radius: 50% 0 50% 50%; background: var(--leaf-dark); }
  .leaf--monstera-bl { left: -6px; top: 393px; width: 82px; height: 76px; border-radius: 50% 50% 50% 0; background: var(--leaf-dark); }
  .leaf--palm-br { left: 340px; top: 398px; width: 130px; height: 70px; border-radius: 90px 0 0 0; }
  .post--yoga .photo { left: 235px; top: 84px; width: 225px; height: 292px;
    background: linear-gradient(180deg, #d9d3da 0%, #e9cdb9 45%, #f1c89d 58%, #b9c4cc 75%, #6f8fa6 100%); }
  .title-band { position: absolute; left: 0; top: 179px; width: 306px; height: 59px; background: var(--mint); }
  .post--yoga .offer { position: absolute; left: 36px; top: 162px; font-size: 12px; }
  .post--yoga .headline { position: absolute; left: 36px; top: 184px; font-size: 18px; font-weight: 600;
    line-height: 29px; text-transform: uppercase; letter-spacing: .2px; }
  .btn-explore { position: absolute; left: 36px; top: 259px; width: 59px; height: 18px;
    background: var(--mint-deep); color: var(--white); font-family: "Roboto", sans-serif; font-size: 8px;
    font-weight: 500; display: flex; align-items: center; justify-content: center; }
  .btn-explore::after { content: ""; position: absolute; left: 3px; top: 3px; width: 59px; height: 18px;
    border: 1px solid var(--mint-deep); z-index: -1; }

  /* Post 2 */
  .diagonal { position: absolute; inset: 0; }
  .post--stones .photo { left: 66px; top: 65px; width: 328px; height: 328px; border-radius: 50%;
    background: radial-gradient(circle at 45% 55%, #d9a680 0%, #c98d68 45%, #e9e5df 80%); }
  .caption { position: absolute; font-size: 15px; font-weight: 600; line-height: 25px; }
  .caption span { display: inline-block; border-bottom: 2px solid var(--white); line-height: 21px; }
  .caption--top { left: 26px; top: 96px; }
  .caption--bottom { left: 307px; top: 309px; }
  .post--stones .offer { position: absolute; left: 0; width: 460px; top: 410px; text-align: center; font-size: 17.5px; }
  .frond--coral { position: absolute; left: 374px; top: 17px; width: 88px; height: 74px;
    background: var(--coral); border-radius: 80% 0 0 80%; opacity: .9; }
  .frond--teal { position: absolute; left: 13px; top: 372px; width: 72px; height: 88px;
    background: var(--mint-deep); border-radius: 60% 60% 20% 20%; opacity: .9; }

  /* Post 3 */
  .post--massage .heading { position: absolute; left: 21px; top: 36px; font-size: 22px; font-weight: 600; line-height: 25px; }
  .post--massage .offer--top { position: absolute; left: 52px; top: 129px; font-size: 21px; }
  .photo--facial { left: 0; top: 168px; width: 215px; height: 226px;
    background: linear-gradient(135deg, #caa58c 0%, #e8c9b1 45%, #b98870 100%); }
  .photo--back { left: 245px; top: 83px; width: 215px; height: 226px;
    background: linear-gradient(160deg, #e9e6e2 0%, #d8ab8c 45%, #8a5a3c 100%); }
  .post--massage .offer--bottom { position: absolute; left: 306px; top: 322px; font-size: 17.5px; }
  .post--massage .subhead { position: absolute; left: 259px; top: 349px; font-family: "Roboto", sans-serif;
    font-weight: 700; font-size: 17.5px; line-height: 25px; }
  .post--massage .brand { left: 0; width: 460px; justify-content: center; top: 418px; }

  /* Post 4 */
  .sand-panel { position: absolute; left: 215px; top: 0; width: 245px; height: 460px; background: var(--sand-texture); }
  .mint-strip { position: absolute; left: 0; top: 90px; width: 215px; height: 347px; background: var(--mint); }
  .post--beach .offer { position: absolute; left: 42px; top: 17px; font-size: 17.5px; }
  .script { position: absolute; left: 42px; top: 48px; font-family: "Yellowtail", cursive; font-size: 28px;
    line-height: 34px; color: var(--sage); }
  .photo-frame { position: absolute; left: 31px; top: 131px; width: 399px; height: 303px; background: var(--white); padding: 6px; }
  .photo-frame .photo { position: static; width: 100%; height: 100%;
    background: linear-gradient(180deg, #dcdfe3 0%, #eef0f1 45%, #c7cfd2 68%, #e6ddcf 78%, #dccfbd 100%); }
</style>
</head>
<body>

  <!-- Post 1: yoga offer -->
  <section class="post post--yoga">
    <div class="leaf leaf--palm-tl" role="img" aria-label="Palm leaf decoration"></div>
    <div class="leaf leaf--monstera-tr" role="img" aria-label="Monstera leaf decoration"></div>
    <div class="leaf leaf--monstera-bl" role="img" aria-label="Monstera leaf decoration"></div>
    <div class="leaf leaf--palm-br" role="img" aria-label="Palm leaf decoration"></div>
    <div class="brand" style="left:161px; top:20px;"><span class="brand__dot"></span>Willowmere</div>
    <div class="photo" role="img" aria-label="Woman meditating on a beach at sunset, arms raised"></div>
    <div class="title-band"></div>
    <p class="offer">20 - 25% OFF</p>
    <h2 class="headline">Lorem ipsum consectetur<br>dolor lit, sed do</h2>
    <a class="btn-explore">EXPLORE</a>
  </section>

  <!-- Post 2: hot stone massage -->
  <section class="post post--stones">
    <svg class="diagonal" width="460" height="460" viewBox="0 0 460 460" aria-hidden="true">
      <polygon points="5,0 460,0 460,460" fill="var(--mint)"/>
    </svg>
    <div class="frond--coral" role="img" aria-label="Coral leaf decoration"></div>
    <div class="frond--teal" role="img" aria-label="Teal leaf decoration"></div>
    <div class="brand" style="left:172px; top:22px;"><span class="brand__dot"></span>Willowmere</div>
    <div class="photo" role="img" aria-label="Woman receiving a hot stone back massage"></div>
    <p class="caption caption--top"><span>Sed ut perspiciatis</span><br><span>unde omnis iste</span></p>
    <p class="caption caption--bottom"><span>Sed ut perspiciatis</span><br><span>unde omnis iste</span></p>
    <p class="offer">20 - 25% off</p>
  </section>

  <!-- Post 3: massage duo -->
  <section class="post post--massage">
    <h2 class="heading">Lorem ipsum dolor amet,<br>consectetur</h2>
    <p class="offer offer--top">20 - 25% off</p>
    <div class="photo photo--facial" role="img" aria-label="Woman receiving a relaxing facial massage"></div>
    <div class="photo photo--back" role="img" aria-label="Back massage with herbal compresses and candles"></div>
    <p class="offer offer--bottom">20 - 25% off</p>
    <p class="subhead">Lorem ipsum dolor<br>consectetur</p>
    <div class="brand"><span class="brand__dot"></span>Willowmere</div>
  </section>

  <!-- Post 4: beach yoga -->
  <section class="post post--beach">
    <div class="sand-panel" role="img" aria-label="Sand texture background"></div>
    <div class="mint-strip"></div>
    <p class="offer">20 - 25% off</p>
    <p class="script">Lorem ipsum dolor amet,<br>consectetur elit,</p>
    <div class="photo-frame">
      <div class="photo" role="img" aria-label="Woman in tree pose on a sandy beach"></div>
    </div>
  </section>

</body>
</html>
```